New Business Card for Software Company

We are looking at rebranding a 10 year old company that specializes in PDF and DWF solutions for Architects and Engineers. We will attach the new company logo that we are going with so you can work with that and complimentary colors.
The sample information we would like on the business card is:
Gerald Pembrook
Vice President
4173 W. Tillman Avenue. STE 306
PMB#417
Mesa, AZ 85316
866-392-7154 US Toll Free
123-581-3064 Cell
gpembrook@vextrolan.com
The old tag line that we had on the business cars was.
Providing Industrial Strength PDF and DWF Solutions to the Global CAD Marketplace.
If you have an idea for a better tag line we are open to that also.
Updates
We would like to thank all of the Designers for their wonderful work. We apologize that we will not have the time to provide feedback to everyone. There is just so many innovative and professional designs that you have all created making our decision even harder.
Target Market(s)
Architects and Engineers
Industry/Entity Type
Business
Look and feel
Each slider illustrates characteristics of the customer's brand and the style your logo design should communicate.

```html
<!DOCTYPE html>
<html lang="en">
<head>
<meta charset="utf-8">
<title>Vextrolan Business Card</title>
<link rel="stylesheet" href="https://fonts.googleapis.com/css2?family=Exo+2:wght@300;400;800&display=swap">
<style>
  :root {
    --backdrop: #e6e8e8;
    --card-white: #f7f7f5;
    --card-slate: #485454;
    --accent-red: #e0401e;
    --accent-orange: #f28a1c;
    --ink-dark: #3a3f41;
    --ink-light: #f4f4f2;
    --tagline: #c9cfcf;
  }
  * { box-sizing: border-box; margin: 0; padding: 0; }
  html, body {
    width: 1200px;
    height: 1000px;
    overflow: hidden;
    background: var(--backdrop);
    font-family: "Exo 2", sans-serif;
  }
  .canvas {
    position: relative;
    width: 1200px;
    height: 1000px;
  }
  .card {
    position: absolute;
    left: 280px;
    width: 640px;
    height: 366px;
    box-shadow: 0 10px 28px rgba(0, 0, 0, 0.16);
  }
  .card--front {
    top: 80px;
    background: var(--card-white);
  }
  .card--back {
    top: 530px;
    background: var(--card-slate);
  }

  /* front */
  .brand-front {
    position: absolute;
    left: 40px;
    top: 30px;
    font-size: 40px;
    font-weight: 800;
    letter-spacing: 0.5px;
    color: var(--accent-red);
  }
  .identity {
    position: absolute;
    left: 28px;
    top: 112px;
    width: 270px;
    padding-left: 12px;
    border-left: 4px solid var(--accent-red);
  }
  .person-name {
    font-size: 30px;
    font-weight: 300;
    color: var(--ink-dark);
    line-height: 1.05;
    letter-spacing: 0.3px;
  }
  .person-role {
    font-size: 14px;
    font-weight: 400;
    color: var(--ink-dark);
    padding-bottom: 4px;
    border-bottom: 2px solid var(--accent-red);
  }
  .address {
    position: absolute;
    left: 44px;
    top: 196px;
    font-size: 14px;
    line-height: 1.3;
    color: var(--accent-red);
    font-style: normal;
  }
  .direct-contact {
    position: absolute;
    left: 330px;
    top: 268px;
    font-size: 14px;
    line-height: 1.3;
    color: var(--accent-red);
    font-style: normal;
  }

  /* back */
  .brand-back {
    position: absolute;
    left: 320px;
    top: 130px;
    font-size: 60px;
    font-weight: 800;
    color: var(--ink-light);
    line-height: 1;
  }
  .tagline {
    position: absolute;
    left: 322px;
    top: 204px;
    width: 300px;
    font-size: 14px;
    font-weight: 300;
    line-height: 1.25;
    color: var(--tagline);
  }
</style>
</head>
<body>
<main class="canvas">
  <section class="card card--front" aria-label="Business card front">
    <div class="brand-front">Vextrolan</div>
    <div class="identity">
      <h1 class="person-name">Gerald Pembrook</h1>
      <p class="person-role">Vice President</p>
    </div>
    <address class="address">
      4173 W. Tillman Avenue. STE 306<br>
      PMB#417<br>
      Mesa, AZ 85316<br>
      866-392-7154 US Toll Free
    </address>
    <address class="direct-contact">
      123-581-3064 Cell<br>
      gpembrook@vextrolan.com
    </address>
  </section>

  <section class="card card--back" aria-label="Business card back">
    <div class="brand-back">Vextrolan</div>
    <p class="tagline">Providing Industrial Strength PDF and DWF Solutions to the Global CAD Marketplace.</p>
  </section>
</main>
</body>
</html>
```